Cleaning service website design

We need a new nice web design(logo will be the same) for a new cleaning service Company:

Informations about Company and logo you can take from flyers in attachments.

This is a cleaning service Company which have simple rules and we would like to show that(in checklist form) on website:

- What we do and that we're Cleaning Green

- Why us?

- How much(our pricing is simple)

Also we would like to communicate with clients by some nice/big pictures on website and the most important thing is our phone number and short/fast Freestimate.

Also there should be some space for description about our Company.

Generally all information on main page can be short: about us, about service(what we do), last reviews, tips (for example: Tip of the week) and other can be some introduction to subpage where will be more information.

There will be few subpages like: About us, About our service, Photos(Before and after), Reviews , Tips, FAQ, Contact, Looking for a Job? - most of them will be just text so you can project just one example.

```html
<!DOCTYPE html>
<html lang="en">
<head>
<meta charset="utf-8">
<title>Tidy Nest – Home Cleaning</title>
<link href="https://fonts.googleapis.com/css2?family=Ubuntu:wght@400&family=Roboto:wght@300;400&family=PT+Sans:wght@400;700&family=Yanone+Kaffeesatz:wght@300;400&display=swap" rel="stylesheet">
<style>
:root{
  --blue:#0a5cad;
  --blue-dark:#0b4f98;
  --green:#6fbe62;
  --green-text:#5aae4c;
  --sky:#e3eff2;
  --ink:#333;
  --grey:#888;
}
*{margin:0;padding:0;box-sizing:border-box}
html,body{width:1200px;height:1200px;overflow:hidden}
body{position:relative;background:#fff;font-family:"Roboto",sans-serif;color:var(--ink)}
.abs{position:absolute}
.bg-top{left:0;top:0;width:1200px;height:117px;background:linear-gradient(#e9f3f5,#d6e8ec)}
.bg-band{left:0;top:117px;width:1200px;height:270px;background:var(--green);border-top:2px solid var(--blue);border-bottom:2px solid var(--blue)}
.bg-low{left:0;top:387px;width:1200px;height:562px;background:var(--sky)}
.card{left:200px;top:24px;width:801px;height:1146px;background:#fff;border:2px solid var(--blue);border-radius:8px;box-shadow:0 0 14px rgba(0,0,0,.25)}
.brand{left:222px;top:40px;display:flex;align-items:center;gap:10px}
.brand-dot{width:34px;height:34px;border-radius:50%;background:var(--green)}
.brand-name{font-family:"Ubuntu",sans-serif;font-size:34px;color:var(--blue)}
.call{left:789px;top:36px;width:190px;text-align:left;font-family:"Yanone Kaffeesatz",sans-serif;line-height:1}
.call .lead{font-size:32px;color:var(--green-text);font-weight:300}
.call .num{font-size:31px;color:#222;font-family:"PT Sans",sans-serif;white-space:nowrap;margin-top:2px}
.nav{left:440px;top:113px;font-family:"PT Sans",sans-serif;font-size:13px;letter-spacing:1.7px;color:var(--blue);white-space:nowrap}
.nav a{color:var(--blue);text-decoration:none}
.nav a.on{color:var(--green-text)}
.nav span{margin:0 4px}
.pricing{left:214px;top:137px;width:213px;height:250px;background:var(--green);border:3px solid var(--blue);color:#fff;font-family:"Yanone Kaffeesatz",sans-serif;text-align:center}
.pricing h2{font-weight:300;font-size:38px;text-align:left;padding:25px 0 0 14px;line-height:.9}
.pricing h2 em{display:block;padding-left:80px;color:var(--blue);font-size:44px;font-style:normal}
.pricing ul{list-style:none;font-size:17px;font-weight:300;margin-top:12px;line-height:18px}
.pricing .note{color:var(--blue);font-size:14px;line-height:15px;margin-top:6px;font-weight:300}
.pricing .small{font-size:10px;margin-top:4px}
.hero{left:439px;top:137px;width:542px;height:250px;border:2px solid var(--blue);background:linear-gradient(170deg,#c9d7c8 0%,#e7a46b 30%,#d9763f 70%,#b45a2c 100%)}
.expect{left:216px;top:416px;width:213px;height:547px;background:linear-gradient(var(--blue-dark) 55%,#5f95cf 85%,#a8c7e6);color:#fff;font-family:"PT Sans",sans-serif;font-size:12px;line-height:15.5px;padding:13px 10px 0 10px}
.expect h3{font-family:"Ubuntu",sans-serif;font-weight:400;font-size:20px;text-decoration:underline;text-underline-offset:3px;margin:0 0 14px 0}
.expect p{margin-bottom:15px}
.contact{left:231px;top:1003px;font-size:10.5px;color:var(--grey);line-height:15.5px}
.contact .name{color:var(--blue);margin-bottom:6px}
h1,h2.sec{font-family:"Ubuntu",sans-serif;font-weight:400;color:#333;letter-spacing:-.5px}
.caring{left:456px;top:414px;font-size:29px}
.body{font-weight:300;font-size:13.4px;line-height:17.2px;color:#444}
.p1{left:456px;top:457px;width:506px}
.rule{left:456px;top:570px;width:518px;height:1px;background:#ddd}
.meet{left:456px;top:577px;font-size:29px}
.p2{left:456px;top:623px;width:265px}
.p2 b{font-weight:400;color:#222;font-size:14px}
.p2 u{text-decoration:underline}
.owners{left:735px;top:623px;width:234px;height:183px;border:1px solid var(--blue);background:linear-gradient(#9cc0e8 0%,#b8d0e8 45%,#5d6a5a 75%,#3b3f3a)}
.why{left:455px;top:884px;font-family:"PT Sans",sans-serif;font-size:18px;color:#222}
.why b{font-family:"Ubuntu",sans-serif;font-weight:400;color:var(--blue);margin-left:8px}
.family{left:457px;top:918px;width:247px;height:122px;border:1px solid #999;background:linear-gradient(120deg,#c9a36b,#e9d8b8 50%,#a98758)}
.perks{left:456px;top:1050px;list-style:none;font-family:"PT Sans",sans-serif;font-size:11px;line-height:17.2px;letter-spacing:.3px}
.more{left:657px;top:1124px;width:38px;height:21px;background:var(--blue);color:#fff;font-size:10px;border:1px solid #fff;outline:1px solid var(--blue);display:flex;align-items:center;justify-content:center;font-family:"PT Sans",sans-serif}
.serving{left:735px;top:870px;font-family:"PT Sans",sans-serif;color:#222;line-height:1}
.serving .a{font-size:17px}
.serving .b{font-size:27px;margin-top:3px}
.map{left:734px;top:923px;width:235px;height:144px;background:linear-gradient(120deg,#efe9d4 0%,#f3ecd8 55%,#a9c2e2 75%)}
.callbox{left:734px;top:1067px;width:235px;height:77px;background:var(--green);text-align:right;font-family:"Yanone Kaffeesatz",sans-serif;color:#222;padding:0 8px}
.callbox .t{font-size:24px;font-weight:300;line-height:24px}
.callbox .n{font-size:29px;color:#fff;text-align:center;line-height:30px}
.callbox .w{font-size:18px;text-align:center;line-height:18px}
.base{left:735px;top:1151px;width:236px;height:1px;background:#ddd}
.foot-line{left:460px;top:1181px;width:236px;height:1px;background:#ccc}
</style>
</head>
<body>
<div class="abs bg-top"></div>
<div class="abs bg-band"></div>
<div class="abs bg-low"></div>
<div class="abs card"></div>

<div class="abs brand"><div class="brand-dot"></div><div class="brand-name">Tidy Nest</div></div>
<div class="abs call"><div class="lead">Call us Today!</div><div class="num">555-014-2290</div></div>
<nav class="abs nav"><a class="on" href="#">Home</a><span>|</span><a href="#">About Us</a><span>|</span><a href="#">Our Services</a><span>|</span><a href="#">Gallery</a><span>|</span><a href="#">Reviews</a><span>|</span><a href="#">Tips</a><span>|</span><a href="#">FAQs</a><span>|</span><a href="#">Careers</a></nav>

<section class="abs pricing">
  <h2>Pricing is...<em>simple.</em></h2>
  <ul><li>$79 for homes less than 1000 sq ft</li><li>$89 for homes 1000-1800 sq ft</li><li>$99 for homes 1800-2600 sq ft</li></ul>
  <p class="note">*If your home is larger than 2600 sq ft<br>please call for a quote.</p>
  <p class="small">*rates are for regular service*</p>
</section>
<div class="abs hero" role="img" aria-label="Photo of a clean terracotta tiled floor with potted plants by a sunny window"></div>

<aside class="abs expect">
  <h3>What To Expect</h3>
  <p>Thoroughly clean your bathrooms, including toilet, sink, shower and tub</p>
  <p>Carefully clean the kitchen, including the sink, countertops and outside of appliances</p>
  <p>Tidy up around the house</p>
  <p>Dusting of surfaces</p>
  <p>Making mirrors shine</p>
  <p>Make beds</p>
  <p>Vacuuming rugs and carpeted areas</p>
  <p>Cleaning of hardwood/tile/linoleum floors</p>
  <p>Emptying garbage</p>
  <p>We take pride in our work and want to keep all of our customers happy. Let us know if you have special requests. If you are not satisfied with your house cleaning for any reason, please contact us and we will make it right. You can trust us to take care of your home as if it was our own.</p>
</aside>
<div class="abs contact"><div class="name">Tidy Nest</div>Telephone:<br>FAX:<br>E-mail:</div>

<h1 class="abs caring">It’s About Caring, Not Just Cleaning</h1>
<p class="abs body p1">Have you ever wondered what it would be like if your life was simpler? We’re here to help you get there by taking over the chore of house cleaning. With our help you’ll have more time to spend on the things that matter most to you. With Tidy Nest you not only get a professional service, but you get it at an affordable price. The owner makes it a point to be at each and every cleaning to assure your needs are met</p>
<div class="abs rule"></div>
<h2 class="abs sec meet">Meet Anna and Mark Kowal</h2>
<div class="abs body p2"><p>We are Mark and Anna Kowal and we have <u>personally</u> experienced the struggle of finding a reliable and affordable maid service. We understand how busy life can be and cleaning is one of the tasks that falls off the list when you’re stretched too thin. <b>We are here to help!</b> Let Tidy Nest take care of the house cleaning so you can focus on the more important things in life.</p><br><p>Halton, Burlington, Oakville and Milton residents can count on us to make your home sparkle from top to bottom!</p></div>
<div class="abs owners" role="img" aria-label="Photo of the two owners standing outdoors on a sunny day"></div>

<div class="abs why">Why Choose<b>Tidy Nest</b></div>
<div class="abs family" role="img" aria-label="Photo of a smiling family with their dog on a sofa"></div>
<ul class="abs perks"><li>• Locally Owned &amp; Operated</li><li>• Reliable &amp; Affordable</li><li>• All Supplies Provided</li><li>• Green Cleaning</li><li>• Pet Friendly</li><li>• No Contracts</li></ul>
<div class="abs more">More</div>

<div class="abs serving"><div class="a">Now Serving</div><div class="b">the Halton Region</div></div>
<div class="abs map" role="img" aria-label="Road map of the Halton region beside the lake"></div>
<div class="abs callbox"><div class="t">call today!</div><div class="n">555-014-2290</div><div class="w">www.TidyNestCleaning.example</div></div>
<div class="abs base"></div>
<div class="abs foot-line"></div>
</body>
</html>
```